Business Card Design

Electrical Contracting buisness
need a buisness card relating to that buisness

Reason: Just need to discuss with partner

Industry/Entity Type

Business

Contact Information for Business Card

Dale Fenwick Electrical
0431 756 918
dalefenwick7@mailnest.example
REC 58714

```html
<!DOCTYPE html>
<html lang="en">
<head>
<meta charset="utf-8">
<title>Dale Fenwick Electrical – Business Card</title>
<link rel="stylesheet" href="https://fonts.googleapis.com/css2?family=Questrial&display=swap">
<style>
  :root {
    --page-bg: #cfd6d1;
    --card-dark: #151718;
    --card-dark-soft: #2a2e30;
    --card-light: #ffffff;
    --accent-yellow: #e8e41a;
    --ring-white: #f4f4f4;
    --ink: #111111;
  }
  * { margin: 0; padding: 0; box-sizing: border-box; }
  html, body {
    width: 1200px;
    height: 1000px;
    overflow: hidden;
    background: var(--page-bg);
  }
  .canvas {
    position: relative;
    width: 1200px;
    height: 1000px;
    display: flex;
    align-items: center;
    justify-content: center;
  }
  .business-card {
    position: relative;
    width: 900px;
    height: 514px;
    background: var(--card-light);
    box-shadow: 0 18px 40px rgba(0, 0, 0, 0.25);
    overflow: hidden;
    font-family: "Questrial", "Century Gothic", sans-serif;
  }
  .card-band {
    position: absolute;
    top: 0;
    left: 0;
    width: 100%;
    height: 250px;
    background: radial-gradient(ellipse at 60% 45%, var(--card-dark-soft) 0%, var(--card-dark) 70%);
  }
  .brand-ring {
    position: absolute;
    top: 72px;
    left: 592px;
    width: 108px;
    height: 108px;
  }
  .brand-name {
    position: absolute;
    top: 192px;
    left: 318px;
    color: var(--accent-yellow);
    font-size: 40px;
    letter-spacing: 0.5px;
    white-space: nowrap;
  }
  .contact-list {
    position: absolute;
    top: 272px;
    left: 300px;
    list-style: none;
    color: var(--ink);
    font-size: 31px;
    line-height: 44px;
  }
  .contact-phone { padding-left: 100px; }
  .contact-email { padding-left: 0; }
  .contact-licence { padding-left: 40px; }
</style>
</head>
<body>
  <main class="canvas">
    <article class="business-card">
      <div class="card-band"></div>
      <svg class="brand-ring" viewBox="0 0 108 108" aria-hidden="true">
        <circle cx="54" cy="54" r="48" fill="none" stroke="var(--ring-white)" stroke-width="6"/>
      </svg>
      <h1 class="brand-name">Dale Fenwick Electrical</h1>
      <ul class="contact-list">
        <li class="contact-phone">0431 756 918</li>
        <li class="contact-email">dalefenwick7@mailnest.example</li>
        <li class="contact-licence">REC 58714</li>
      </ul>
    </article>
  </main>
</body>
</html>
```